Start-up Cleaning Business Needs Professional Business Cards

Marta's Butler Cleaning, LLC, is a start-up business based in the Northern Virginia suburbs of Washington, DC. MBC provides cleaning and housekeeping services for homes and offices. We have three core values:

1. We are personal. We value knowing and being known by our customers and each other. If you want nameless, faceless service, you should choose another provider. We put "personal" at the front of the list, because it is most important to us; the design we choose will convey this value.

2. Like a hotel concierge, we are professional in attitude, posture, communication and processes.

3. Like a hotel concierge, we solve problems with a can-do attitude and never make excuses.

Our uniforms are khaki pants with pink polo shirts.

Our logo is attached. There are other symbols, not represented in our logo, that may convey our values well, such as a top hat and bow tie, magnifying glass, desk bell, etc.

Please include fields for an individual's name and title, office phone number, mobile phone number, email address and website address (www.martasbutlercleaning.example).

Standard U.S. size: 2" x 3.5"
Updates

I should have mentioned that the purpose of all our advertising - business cards included - is to motivate potential customers to call or email to arrange a free in-home estimate.

```html
<!DOCTYPE html>
<html lang="en">
<head>
<meta charset="utf-8">
<title>Marta's Butler Cleaning, LLC – Business Cards</title>
<link rel="stylesheet" href="https://fonts.googleapis.com/css2?family=Arimo:wght@400;700&display=swap">
<style>
  :root {
    --backdrop: #e9e6e1;
    --card: #ffffff;
    --ink: #3a3a3a;
    --ink-soft: #4a4a4a;
    --pink: #e0318f;
    --pink-soft: #f2c3da;
    --art-dark: #6b3a3a;
    --art-pink: #e56aa6;
  }
  * { box-sizing: border-box; margin: 0; padding: 0; }
  html, body {
    width: 1050px; height: 1200px; overflow: hidden;
    background: var(--backdrop);
    font-family: "Arimo", Arial, sans-serif;
    color: var(--ink);
  }
  .canvas { position: relative; width: 1050px; height: 1200px; }
  .card {
    position: absolute; width: 919px; height: 526px;
    background: var(--card);
    box-shadow: 0 4px 14px rgba(0,0,0,0.18);
  }
  .card--front { left: 63px; top: 52px; }
  .card--back { left: 79px; top: 612px; }

  .company-name {
    position: absolute; left: 67px; top: 70px;
    font-size: 34px; font-weight: 400; color: var(--ink-soft);
    letter-spacing: 0.5px;
  }
  .person-name {
    position: absolute; left: 67px; top: 172px;
    font-size: 31px; font-weight: 700; color: var(--ink-soft);
  }
  .person-title {
    position: absolute; left: 67px; top: 216px;
    font-size: 21px; color: var(--pink);
  }
  .contact-list {
    position: absolute; left: 67px; top: 265px; list-style: none;
  }
  .contact-list li {
    display: flex; align-items: center; gap: 8px;
    height: 38px; font-size: 23px; color: var(--ink-soft);
  }
  .contact-list svg { width: 18px; height: 18px; flex: none; fill: var(--pink); }
  .call-to-action {
    position: absolute; left: 0; right: 0; top: 463px;
    text-align: center; font-size: 34px; color: var(--ink);
  }
  .illustration-faint {
    position: absolute; left: 577px; top: 9px; width: 280px; height: 438px;
    background: linear-gradient(180deg, #f1eeee 0%, #f7e4ee 70%, #f3dde8 100%);
    border-radius: 6px; opacity: 0.8;
  }

  .illustration-main {
    position: absolute; left: 87px; top: 39px; width: 263px; height: 347px;
    background: linear-gradient(180deg, #d8c4c4 0%, #ef9fc6 55%, #e3a9a0 100%);
    border-radius: 6px;
  }
  .brand-mark {
    position: absolute; left: 40px; width: 320px; text-align: center;
    color: var(--ink-soft); font-weight: 400;
  }
  .brand-mark--name { top: 395px; font-size: 62px; line-height: 1; }
  .brand-mark--tag { top: 467px; font-size: 20px; letter-spacing: 1px; }
  .back-website {
    position: absolute; left: 371px; top: 246px;
    font-size: 23px; letter-spacing: 1.5px; color: var(--ink);
  }
</style>
</head>
<body>
<main class="canvas">
  <section class="card card--front" aria-label="Business card front">
    <div class="illustration-faint" role="img" aria-label="Faint illustration of a housekeeper in a pink uniform mopping the floor"></div>
    <h1 class="company-name">Marta's Butler Cleaning, LLC</h1>
    <p class="person-name">Individuals name</p>
    <p class="person-title">Title</p>
    <ul class="contact-list">
      <li>
        <svg viewBox="0 0 20 20" aria-hidden="true"><path d="M5 2l3 3-2 3c1 2 3 4 5 5l2-2 3 3-2 3C8 17 3 12 2 5z"/></svg>
        (123) 456-7890
      </li>
      <li>
        <svg viewBox="0 0 20 20" aria-hidden="true"><path d="M6 1h8a1 1 0 0 1 1 1v16a1 1 0 0 1-1 1H6a1 1 0 0 1-1-1V2a1 1 0 0 1 1-1zm1 3v10h6V4zm3 11.5a1 1 0 1 0 0 2 1 1 0 0 0 0-2z"/></svg>
        (123) 456-7890
      </li>
      <li>
        <svg viewBox="0 0 20 20" aria-hidden="true"><path d="M1 5h18v11H1zm1.5 1.2L10 11l7.5-4.8V6h-15z"/></svg>
        info@martasbutlercleaning.example
      </li>
      <li>
        <svg viewBox="0 0 20 20" aria-hidden="true"><path d="M10 1a9 9 0 1 0 0 18 9 9 0 0 0 0-18zm0 1.6c.9 0 2 1.8 2.4 4.4H7.6C8 4.4 9.1 2.6 10 2.6zM3 9h3.4a14 14 0 0 0 0 2H3a7 7 0 0 1 0-2zm4.4 0h5.2a13 13 0 0 1 0 2H7.4a13 13 0 0 1 0-2zm6.2 0H17a7 7 0 0 1 0 2h-3.4a14 14 0 0 0 0-2zM7.6 13h4.8c-.4 2.6-1.5 4.4-2.4 4.4S8 15.6 7.6 13z"/></svg>
        www.martasbutlercleaning.example
      </li>
    </ul>
    <p class="call-to-action">Call or email to arrange a free in-home estimate</p>
  </section>

  <section class="card card--back" aria-label="Business card back">
    <div class="illustration-main" role="img" aria-label="Illustration of a housekeeper in a pink uniform and headband mopping the floor"></div>
    <p class="brand-mark brand-mark--name">Marta's</p>
    <p class="brand-mark brand-mark--tag">Butler Cleaning</p>
    <p class="back-website">www.martasbutlercleaning.example</p>
  </section>
</main>
</body>
</html>
```